Dental Office Business Card

We need a business card for our pediatric dentistry office.
On one side the design needs to contain the following:
our logo (attached)
Vento Pediatric Grins
Soraya Kadbelani, DDS
Board Certified Pediatric Dentist
Tel: (555) 318-2747)
Fax: (555) 264-8031
Email: info@ventopediatricgrins.example
Web: www.ventopediatricgrins.example
Address: 41 Brindle Ave, Suite 208, Larkmoor, XT 02099

On the other side of the card, the design needs to have an appointment reminder (date and time as well as day of the week) similar to the design attached (no need for appointment reason “For”)

```html
<!DOCTYPE html>
<html lang="en">
<head>
<meta charset="utf-8">
<title>Vento Pediatric Grins – Business Card</title>
<link rel="stylesheet" href="https://fonts.googleapis.com/css2?family=Montserrat:wght@400;500;600;700&display=swap">
<style>
  :root {
    --mint: #a8d5ab;
    --ink: #231f20;
    --paper: #ffffff;
    --stage: #e9eae8;
  }
  * { box-sizing: border-box; margin: 0; padding: 0; }
  html, body { width: 1200px; height: 900px; overflow: hidden; }
  body {
    background: var(--stage);
    font-family: "Montserrat", sans-serif;
    color: var(--ink);
    position: relative;
  }
  .card {
    position: absolute;
    left: 270px;
    width: 660px;
    height: 378px;
    background: var(--paper);
    overflow: hidden;
    box-shadow: 0 6px 18px rgba(0,0,0,.18);
  }
  .card--reminder { top: 52px; }
  .card--contact { top: 470px; }
  .card__shapes { position: absolute; inset: 0; width: 100%; height: 100%; }

  .brand {
    position: absolute;
    display: flex;
    align-items: center;
    gap: 12px;
    font-weight: 700;
    color: var(--ink);
    white-space: nowrap;
  }
  .brand__dot {
    width: 34px; height: 34px;
    border-radius: 50%;
    background: var(--mint);
    flex: none;
  }
  .card--reminder .brand { top: 48px; left: 0; right: 0; justify-content: center; font-size: 30px; }
  .card--contact .brand { top: 200px; right: 30px; font-size: 25px; }

  /* Appointment reminder */
  .reminder {
    position: absolute;
    top: 138px;
    left: 0; right: 0;
    text-align: center;
    font-size: 16px;
    font-weight: 500;
  }
  .reminder__row { display: flex; justify-content: center; align-items: center; gap: 12px; margin-bottom: 18px; }
  .blank { display: inline-block; border-bottom: 1.5px solid var(--ink); height: 18px; }
  .blank--short { width: 46px; }
  .blank--long { width: 110px; }
  .blank--time { width: 140px; }
  .slash { margin: 0 2px; }
  .option { display: inline-flex; align-items: center; gap: 5px; }
  .box { width: 14px; height: 14px; border: 1.5px solid var(--mint); display: inline-block; }

  /* Contact side */
  .person {
    position: absolute;
    top: 36px; left: 36px;
    color: var(--paper);
  }
  .person__name { font-size: 22px; font-weight: 700; }
  .person__title { font-size: 15px; font-weight: 500; margin-top: 4px; }
  .contact {
    position: absolute;
    top: 214px; left: 40px;
    font-size: 14px;
    line-height: 1.4;
  }
  .contact__address { margin-bottom: 6px; font-size: 15px; }
  .contact__line { display: flex; align-items: center; gap: 8px; }
  .contact__icon { width: 14px; height: 14px; flex: none; fill: var(--mint); }
</style>
</head>
<body>

<section class="card card--reminder" aria-label="Appointment reminder side">
  <svg class="card__shapes" viewBox="0 0 660 378" preserveAspectRatio="none" aria-hidden="true">
    <polygon points="300,350 660,290 660,378 290,378" fill="var(--mint)"/>
    <polygon points="0,350 300,350 290,378 0,378" fill="var(--ink)"/>
  </svg>
  <div class="brand"><span class="brand__dot"></span>Vento Pediatric Grins</div>
  <div class="reminder">
    <div class="reminder__row">
      <span>Date :</span>
      <span class="blank blank--short"></span><span class="slash">/</span>
      <span class="blank blank--short"></span><span class="slash">/</span>
      <span class="blank blank--long"></span>
    </div>
    <div class="reminder__row">
      <span class="option"><span class="box"></span>Mon</span>
      <span class="option"><span class="box"></span>Tue</span>
      <span class="option"><span class="box"></span>Wed</span>
      <span class="option"><span class="box"></span>Thu</span>
      <span class="option"><span class="box"></span>Fri</span>
      <span class="option"><span class="box"></span>Sat</span>
      <span class="option"><span class="box"></span>Sun</span>
    </div>
    <div class="reminder__row">
      <span>Time :</span>
      <span class="blank blank--time"></span>
      <span class="option"><span class="box"></span>A.M</span>
      <span class="option"><span class="box"></span>P.M</span>
    </div>
  </div>
</section>

<section class="card card--contact" aria-label="Contact side">
  <svg class="card__shapes" viewBox="0 0 660 378" preserveAspectRatio="none" aria-hidden="true">
    <path d="M0,0 H620 C500,18 410,55 330,100 C250,145 130,155 0,150 Z" fill="var(--mint)"/>
    <path d="M0,150 C130,155 250,145 330,100 C410,55 500,18 620,0 H640 C540,30 450,85 380,135 C300,190 150,200 0,196 Z" fill="var(--ink)"/>
    <path d="M40,204 C190,202 300,180 385,132 C470,80 560,32 660,16" fill="none" stroke="var(--mint)" stroke-width="3"/>
    <polygon points="420,350 660,300 660,378 410,378" fill="var(--mint)"/>
    <polygon points="0,350 420,350 410,378 0,378" fill="var(--ink)"/>
    <polygon points="412,378 422,350 428,350 418,378" fill="var(--paper)"/>
  </svg>

  <div class="person">
    <div class="person__name">Soraya Kadbelani, DDS</div>
    <div class="person__title">Board Certified Pediatric Dentist</div>
  </div>

  <div class="brand"><span class="brand__dot"></span>Vento Pediatric Grins</div>

  <div class="contact">
    <div class="contact__address">41 Brindle Ave, Suite 208,<br>Larkmoor, XT 02099</div>
    <div class="contact__line">
      <svg class="contact__icon" viewBox="0 0 16 16" aria-label="Phone"><path d="M3 1h3l1 4-2 1.5a9 9 0 0 0 4.5 4.5L11 9l4 1v3a2 2 0 0 1-2 2A12 12 0 0 1 1 3a2 2 0 0 1 2-2z"/></svg>
      <span>(555) 318-2747)</span>
    </div>
    <div class="contact__line">
      <svg class="contact__icon" viewBox="0 0 16 16" aria-label="Fax"><rect x="4" y="1" width="8" height="4"/><rect x="1" y="6" width="14" height="6" rx="1"/><rect x="4" y="10" width="8" height="5"/></svg>
      <span>(555) 264-8031</span>
    </div>
    <div class="contact__line">
      <svg class="contact__icon" viewBox="0 0 16 16" aria-label="Email"><rect x="1" y="3" width="14" height="10"/><polyline points="1,3 8,9 15,3" fill="none" stroke="var(--paper)" stroke-width="1.2"/></svg>
      <span>info@ventopediatricgrins.example</span>
    </div>
    <div class="contact__line">
      <svg class="contact__icon" viewBox="0 0 16 16" aria-label="Website"><circle cx="8" cy="8" r="7"/><path d="M1 8h14M8 1c-3 3-3 11 0 14M8 1c3 3 3 11 0 14" fill="none" stroke="var(--paper)" stroke-width="1"/></svg>
      <span>www.ventopediatricgrins.example</span>
    </div>
  </div>
</section>

</body>
</html>
```